Global social media analytics company needs business card design

We need an updated business card design to align with our new website - plumvantix.com -

I would also like a favicon designed as well.

Target Market(s)

CEOs, CMOs go big companies

Industry/Entity Type

Business

Contact Information for Business Card

Room for the following:
Address
Main telephone
Direct telephone or cell phone
twitter handle

Colors
aaaaaa

Requirements
Must have
• Attention to detail; style.
• Use the logo color from our website - which is gray

```html
<!DOCTYPE html>
<html lang="en">
<head>
<meta charset="utf-8">
<title>Plumvantix Stationery</title>
<link href="https://fonts.googleapis.com/css2?family=Open+Sans:wght@400;600;700&family=Montserrat:wght@400;500&display=swap" rel="stylesheet">
<style>
  :root {
    --backdrop: #e6e6e6;
    --paper: #ffffff;
    --brand-gray: #aaaaaa;
    --band-gray: #9a9a9a;
    --ink: #4a4a4a;
    --ink-soft: #7a7a7a;
    --rule: #c8c8c8;
  }
  * { box-sizing: border-box; margin: 0; padding: 0; }
  html, body { width: 1200px; height: 706px; overflow: hidden; }
  body {
    background: var(--backdrop);
    font-family: "Open Sans", Arial, sans-serif;
    color: var(--ink);
    position: relative;
  }

  /* Brand lockup */
  .brand { display: flex; flex-direction: column; align-items: center; gap: 4px; }
  .brand-dot { border-radius: 50%; background: var(--brand-gray); }
  .brand-name { font-weight: 700; color: var(--brand-gray); letter-spacing: -0.02em; line-height: 1; }

  /* Business cards */
  .card {
    position: absolute;
    width: 320px; height: 183px;
    background: var(--paper);
    box-shadow: 0 2px 0 #d4d4d4, 0 4px 0 #cfcfcf, 0 8px 14px rgba(0,0,0,0.12);
    overflow: hidden;
  }
  .card-front { left: 250px; top: 120px; }
  .card-back { left: 250px; top: 370px; }

  .card-photo {
    position: absolute; inset: 0;
    background: linear-gradient(100deg, #8a6f4e 0%, #c9b08a 22%, #efe4cf 45%, #d8c3a0 62%, #a8865c 82%, #6e5a44 100%);
  }
  .card-veil {
    position: absolute; left: 0; right: 0; top: 58px; height: 70px;
    background: rgba(255,255,255,0.55);
    display: flex; align-items: center; justify-content: center;
  }
  .card-veil .brand-dot { width: 30px; height: 30px; }
  .card-veil .brand-name { font-size: 15px; }

  .card-back .brand { margin-top: 22px; }
  .card-back .brand-dot { width: 30px; height: 30px; }
  .card-back .brand-name { font-size: 14px; }
  .card-person { text-align: center; margin-top: 10px; }
  .person-name { font-size: 12px; letter-spacing: 0.12em; color: var(--ink); }
  .person-title { font-size: 7px; letter-spacing: 0.1em; color: var(--ink-soft); margin-top: 2px; }
  .card-rule { width: 200px; height: 1px; background: var(--rule); margin: 8px auto 6px; }
  .card-contact { font-size: 6.5px; color: var(--ink-soft); text-align: center; line-height: 1.6; }
  .card-contact .icon { display: inline-block; vertical-align: -1px; margin-right: 2px; }
  .card-band {
    position: absolute; left: 0; right: 0; bottom: 0; height: 22px;
    background: var(--band-gray); color: #fff;
    font-family: "Montserrat", Arial, sans-serif; font-size: 8px; letter-spacing: 0.12em;
    display: flex; align-items: center; justify-content: center; gap: 14px;
  }

  /* Letterhead */
  .letterhead {
    position: absolute; left: 650px; top: 30px;
    width: 450px; height: 636px;
    background: var(--paper);
    box-shadow: 0 2px 0 #dadada, 0 4px 0 #d2d2d2, 0 10px 18px rgba(0,0,0,0.12);
    display: flex; flex-direction: column;
  }
  .letterhead .brand { margin-top: 34px; }
  .letterhead .brand-dot { width: 40px; height: 40px; }
  .letterhead .brand-name { font-size: 19px; }
  .letter-meta { text-align: center; font-size: 7.5px; line-height: 1.5; margin-top: 18px; color: var(--ink); }
  .letter-body { padding: 10px 44px 0; font-size: 7.2px; line-height: 1.5; text-align: justify; color: var(--ink); }
  .letter-body p { margin-bottom: 9px; }
  .letter-body p.lead { text-indent: 0; }
  .letter-body p + p { text-indent: 36px; }

  .letter-footer { margin-top: auto; text-align: center; font-family: "Montserrat", Arial, sans-serif; }
  .footer-divider { display: flex; align-items: center; justify-content: center; gap: 8px; margin-bottom: 6px; }
  .footer-divider span { width: 130px; height: 1px; background: var(--rule); }
  .footer-divider .pin { width: 10px; height: 10px; border-radius: 50%; background: var(--brand-gray); }
  .footer-line { font-size: 7.5px; color: var(--ink-soft); letter-spacing: 0.08em; line-height: 1.7; }
  .footer-line .icon { display: inline-block; vertical-align: -1px; margin: 0 2px 0 8px; }
  .letter-band {
    height: 30px; margin-top: 12px; background: var(--band-gray); color: #fff;
    font-size: 9px; letter-spacing: 0.16em;
    display: flex; align-items: center; justify-content: center;
  }
</style>
</head>
<body>

  <section class="card card-front" aria-label="Business card front">
    <div class="card-photo" role="img" aria-label="Blurred warm-toned city street photograph"></div>
    <div class="card-veil">
      <div class="brand">
        <div class="brand-dot"></div>
        <div class="brand-name">plumvantix</div>
      </div>
    </div>
  </section>

  <section class="card card-back" aria-label="Business card back">
    <div class="brand">
      <div class="brand-dot"></div>
      <div class="brand-name">plumvantix</div>
    </div>
    <div class="card-person">
      <div class="person-name">Daniel Mercer</div>
      <div class="person-title">CEO</div>
    </div>
    <div class="card-rule"></div>
    <div class="card-contact">
      <div>2270 Harlow Street, 3rd Fl. Brookfield, MA 02741 USA</div>
      <div>
        <svg class="icon" width="7" height="7" viewBox="0 0 10 10"><circle cx="5" cy="5" r="5" fill="#9a9a9a"/><path d="M3 2.6c.3 2 1.9 3.9 4.2 4.6l.5-1-1.2-.6-.5.5C5.1 5.7 4.5 5 4.3 4.2l.5-.4-.5-1.3z" fill="#fff"/></svg>+1 555 240 3170
        &nbsp;<svg class="icon" width="7" height="7" viewBox="0 0 10 10"><circle cx="5" cy="5" r="5" fill="#9a9a9a"/><path d="M3 2.6c.3 2 1.9 3.9 4.2 4.6l.5-1-1.2-.6-.5.5C5.1 5.7 4.5 5 4.3 4.2l.5-.4-.5-1.3z" fill="#fff"/></svg>+1 555 240 3199
      </div>
    </div>
    <div class="card-band">
      <span>www.plumvantix.com</span>
      <span>@plumvantix</span>
    </div>
  </section>

  <article class="letterhead" aria-label="Letterhead">
    <div class="brand">
      <div class="brand-dot"></div>
      <div class="brand-name">plumvantix</div>
    </div>

    <div class="letter-meta">
      <div>Plumvantix</div>
      <div>December 22, 2011/Revised February 2, 2013</div>
    </div>

    <div class="letter-body">
      <p class="lead">Lorem ipsum dolor sit amet, consectetur adipiscing elit. Sed libero est, pellentesque facilisis tempor eu, pulvinar vitae justo. Praesent bibendum ultricies magna luctus luctus. Suspendisse potenti. Pellentesque habitant morbi tristique senectus et netus et malesuada fames ac turpis egestas. Nullam elit urna, porttitor quis luctus ac, gravida in ante. Vestibulum ante ipsum primis in faucibus orci luctus et ultrices posuere cubilia Curae; Praesent auctor aliquet tempor. Curabitur vel leo quis eros dapibus rutrum. Pellentesque accumsan, diam vel tristique dictum, leo magna pellentesque justo, non ullamcorper sapien justo et dui. Nam et nulla.</p>
      <p>Donec consectetur tempor purus. Nullam turpis lacus, molestie bibendum auctor non, convallis quis mauris. Cum sociis natoque penatibus et magnis dis parturient montes, nascetur ridiculus mus. Aenean feugiat erat sit amet massa semper ullamcorper lobortis massa interdum. Fusce turpis nunc, pellentesque quis accumsan viverra, tempor vel sem. Etiam varius, velit et pretium cursus, lorem massa consequat orci, sit amet interdum turpis nibh ac eros. Nam et tellus nulla, eget congue nisl. Mauris vitae sapien ut quam malesuada suscipit mattis sed nulla. Ut dictum tellus vel metus eleifend tincidunt. Proin aliquet enim sit amet est faucibus nec molestie ligula dignissim. Nam tempor ligula non nunc eleifend tempor. Maecenas fermentum nunc vel diam ultrices vulputate sed vitae elit. Nam vitae dui tortor, quis scelerisque velit. Sed pretium blandit odio, vel malesuada purus convallis.</p>
      <p>Donec consectetur tempor purus. Nullam turpis lacus, molestie bibendum auctor non, convallis quis mauris. Cum sociis natoque penatibus et magnis dis parturient montes, nascetur ridiculus mus. Aenean feugiat erat sit amet massa semper ullamcorper lobortis massa interdum. Fusce turpis nunc, pellentesque quis accumsan viverra, tempor vel sem. Etiam varius, velit et pretium cursus, lorem massa consequat orci, sit amet interdum turpis nibh ac eros. Nam et tellus nulla, eget congue nisl. Mauris dui tortor, quis scelerisque velit. Sed pretium blandit odio, vel malesuada purus convallis vitae. Aliquam erat volutpat.</p>
      <p>Donec consectetur tempor purus. Nullam turpis lacus, molestie bibendum auctor non, convallis quis mauris. Cum sociis natoque penatibus et magnis dis parturient montes, nascetur ridiculus mus. Aenean feugiat erat sit amet massa semper ullamcorper lobortis massa interdum. Fusce turpis nunc, pellentesque quis accumsan viverra, tempor vel sem. Etiam varius, velit et pretium cursus, lorem massa consequat orci, sit amet interdum turpis nibh ac eros. Nam et tellus nulla, eget congue nisl. Mauris vitae sapien ut quam malesuada suscipit mattis sed nulla. Ut dictum tellus vel metus eleifend tincidunt. Proin aliquet enim sit amet est faucibus nec molestie ligula dignissim. Nam tempor ligula non nunc eleifend tempor. Maecenas fermentum nunc vel diam ultrices vulputate sed vitae elit. Nam vitae dui tortor, quis scelerisque velit. Sed pretium blandit odio, vel malesuada purus convallis vitae. Aliquam.</p>
    </div>

    <footer class="letter-footer">
      <div class="footer-divider"><span></span><div class="pin"></div><span></span></div>
      <div class="footer-line">2270 Harlow Street, 3rd Fl. Brookfield, MA 02741 USA</div>
      <div class="footer-line">
        <svg class="icon" width="8" height="8" viewBox="0 0 10 10"><circle cx="5" cy="5" r="5" fill="#9a9a9a"/><path d="M3 2.6c.3 2 1.9 3.9 4.2 4.6l.5-1-1.2-.6-.5.5C5.1 5.7 4.5 5 4.3 4.2l.5-.4-.5-1.3z" fill="#fff"/></svg>+1 555 240 3170
        <svg class="icon" width="8" height="8" viewBox="0 0 10 10"><circle cx="5" cy="5" r="5" fill="#9a9a9a"/><path d="M3 2.6c.3 2 1.9 3.9 4.2 4.6l.5-1-1.2-.6-.5.5C5.1 5.7 4.5 5 4.3 4.2l.5-.4-.5-1.3z" fill="#fff"/></svg>+1 555 240 3199
        <span style="margin-left:8px">@plumvantix</span>
      </div>
      <div class="letter-band">www.plumvantix.com</div>
    </footer>
  </article>

</body>
</html>
```